Accounting Business needs double sided DL flyer design

We need a double sided DL flyer designed,
Front side with logo, web address and our short intro.
Backside to have a list of services.
Our colours are blue and a concrete grey colour. Look at our website for a feel for our colour scheme.
www.lanternwellgroup.com.au
I have included the pic from our website to possibly use but we are also open to new creative ideas.
Target Market(s)
Our target market are proactive business owners, particularly in the wine and hospitality industry.
Industry/Entity Type
Business
Look and feel

```html
<!DOCTYPE html>
<html lang="en">
<head>
<meta charset="utf-8">
<title>Lanternwell Group – DL Flyer</title>
<link href="https://fonts.googleapis.com/css2?family=Oswald:wght@300;400;500&family=Poppins:wght@600;700&family=Satisfy&display=swap" rel="stylesheet">
<style>
  :root{
    --bg:#e9e6e1;
    --teal:#2d9ab8;
    --teal-light:#3fb7c4;
    --navy:#2f4f9c;
    --blue:#1f78a8;
    --ink:#1a1a1a;
    --white:#ffffff;
    --paper:#f4f4f4;
  }
  *{margin:0;padding:0;box-sizing:border-box}
  html,body{width:1200px;height:717px;overflow:hidden;background:var(--bg)}
  .canvas{position:relative;width:1200px;height:717px}
  .flyer{position:absolute;top:38px;width:302px;height:640px;background:var(--white);overflow:hidden;box-shadow:0 2px 8px rgba(0,0,0,.12)}
  .flyer--front{left:262px}
  .flyer--back{left:636px;background:var(--paper)}
  .flyer svg.shapes{position:absolute;inset:0}

  /* front */
  .brand{position:absolute;left:18px;top:20px;font-family:'Oswald',sans-serif;font-weight:500;font-size:20px;color:var(--navy);letter-spacing:.5px}
  .tagline{position:absolute;right:16px;top:66px;text-align:right;color:var(--white);font-family:'Poppins',sans-serif;font-weight:700;line-height:1.05}
  .tagline .big{font-size:22px;display:block}
  .tagline .small{font-size:17px;display:block}
  .intro{position:absolute;left:22px;top:360px;color:var(--white);font-family:'Oswald',sans-serif;font-weight:300;font-size:29px;line-height:1.12}
  .contact{position:absolute;bottom:24px;font-family:'Oswald',sans-serif;font-size:9px;color:var(--ink);text-align:center;white-space:nowrap}
  .contact--phone{left:8px;width:70px}
  .contact--web{left:78px;width:118px;font-size:8.5px}
  .icon-dot{display:block;margin:0 auto 8px;width:34px;height:34px;border-radius:50%;background:var(--blue);position:relative}
  .contact--phone .icon-dot{background:var(--teal)}
  .contact--web .icon-dot{background:var(--navy)}
  .icon-dot svg{position:absolute;left:9px;top:9px}

  /* back */
  .header-photo{position:absolute;left:0;top:0;width:302px;height:120px;background:linear-gradient(90deg,#d9dadc 0%,#b9bbbe 55%,#6f7377 100%)}
  .back-brand{position:absolute;left:18px;top:18px;font-family:'Oswald',sans-serif;font-weight:500;font-size:20px;color:var(--navy);letter-spacing:1px;line-height:1.1}
  .back-brand small{display:block;font-size:9px;letter-spacing:3px}
  .section-band{position:absolute;left:0;top:80px;width:240px;height:40px;background:rgba(255,255,255,.75);padding:4px 0 0 30px;font-family:'Oswald',sans-serif;font-size:27px;font-weight:300;color:#444}
  .section-band span{color:var(--teal)}
  .services{position:absolute;list-style:none;font-family:'Oswald',sans-serif;font-weight:300;font-size:12.5px;color:var(--ink)}
  .services li{display:flex;align-items:center;gap:6px;height:21px}
  .services--main{left:18px;top:134px}
  .services--extra{left:196px;top:180px}
  .tick{width:11px;height:9px;flex:none}
  .why{position:absolute;left:18px;top:282px;font-family:'Oswald',sans-serif;font-size:18px;color:var(--ink)}
  .why span{color:var(--teal)}
  .reasons{position:absolute;left:18px;top:312px;width:268px;list-style:none;font-family:'Satisfy',cursive;font-size:13px;line-height:1.05;color:var(--ink)}
  .reasons li{display:flex;gap:6px;margin-bottom:6px}
  .reasons .tick{margin-top:3px}
  .cta{position:absolute;left:18px;top:474px;display:flex;gap:10px;align-items:center}
  .cta .icon-dot{margin:0;width:40px;height:40px;background:var(--blue)}
  .cta .icon-dot svg{left:12px;top:12px}
  .cta-text{font-family:'Oswald',sans-serif;font-size:19px;color:var(--blue);line-height:1.15;text-transform:uppercase}
  .footer{position:absolute;left:0;bottom:0;width:302px;height:38px;background:var(--ink);display:flex;align-items:center;justify-content:space-around;font-family:'Oswald',sans-serif;font-size:9px;color:var(--white)}
  .footer span{display:flex;align-items:center;gap:5px}
  .footer i{display:inline-block;width:10px;height:8px;background:var(--teal)}
</style>
</head>
<body>
<div class="canvas">

  <section class="flyer flyer--front">
    <svg class="shapes" width="302" height="640" viewBox="0 0 302 640">
      <defs>
        <linearGradient id="stairs" x1="0" y1="0" x2="0" y2="1">
          <stop offset="0" stop-color="#e7e6e3"/>
          <stop offset=".55" stop-color="#b9b8b5"/>
          <stop offset="1" stop-color="#53575c"/>
        </linearGradient>
      </defs>
      <rect x="210" y="170" width="92" height="470" fill="url(#stairs)" role="img" aria-label="Photo of concrete steps"/>
      <polygon points="100,40 302,40 302,190 0,300 0,225" fill="var(--teal)"/>
      <polygon points="210,226 302,190 302,240 210,310" fill="var(--teal-light)"/>
      <polygon points="0,300 210,226 210,640 0,640" fill="var(--ink)"/>
      <rect x="0" y="520" width="198" height="120" fill="var(--white)"/>
    </svg>
    <div class="brand">LANTERNWELL</div>
    <p class="tagline"><span class="big">A</span><span class="big">guiding hand,</span><span class="small">a voice of reason</span></p>
    <p class="intro">A true<br>sounding<br>board for<br>success</p>
    <div class="contact contact--phone">
      <span class="icon-dot"><svg width="16" height="16" viewBox="0 0 16 16"><circle cx="8" cy="5" r="3.2" fill="#fff"/><path d="M2 15c0-4 3-6 6-6s6 2 6 6z" fill="#fff"/></svg></span>
      0400 118 274
    </div>
    <div class="contact contact--web">
      <span class="icon-dot"><svg width="16" height="16" viewBox="0 0 16 16"><path d="M8 2 1 8h2v6h4v-4h2v4h4V8h2z" fill="#fff"/></svg></span>
      www.lanternwellgroup.com.au
    </div>
  </section>

  <section class="flyer flyer--back">
    <div class="header-photo" role="img" aria-label="Photo of city office buildings"></div>
    <div class="back-brand">LANTERNWELL GROUP<small>BUSINESS ADVISORS</small></div>
    <div class="section-band">OUR <span>SERVICE</span></div>

    <ul class="services services--main">
      <li><svg class="tick" viewBox="0 0 11 9"><rect width="11" height="9" fill="var(--teal)"/><path d="M2 4.5 4.5 7 9 2" stroke="#fff" stroke-width="1.5" fill="none"/></svg>Taxation Compliance</li>
      <li><svg class="tick" viewBox="0 0 11 9"><rect width="11" height="9" fill="var(--teal)"/><path d="M2 4.5 4.5 7 9 2" stroke="#fff" stroke-width="1.5" fill="none"/></svg>Financial &amp; Management Reporting</li>
      <li><svg class="tick" viewBox="0 0 11 9"><rect width="11" height="9" fill="var(--teal)"/><path d="M2 4.5 4.5 7 9 2" stroke="#fff" stroke-width="1.5" fill="none"/></svg>Self-Managed Superannuation</li>
      <li><svg class="tick" viewBox="0 0 11 9"><rect width="11" height="9" fill="var(--teal)"/><path d="M2 4.5 4.5 7 9 2" stroke="#fff" stroke-width="1.5" fill="none"/></svg>Business Support Services</li>
      <li><svg class="tick" viewBox="0 0 11 9"><rect width="11" height="9" fill="var(--teal)"/><path d="M2 4.5 4.5 7 9 2" stroke="#fff" stroke-width="1.5" fill="none"/></svg>Business Planning</li>
      <li><svg class="tick" viewBox="0 0 11 9"><rect width="11" height="9" fill="var(--teal)"/><path d="M2 4.5 4.5 7 9 2" stroke="#fff" stroke-width="1.5" fill="none"/></svg>KPIs &amp; Performance Monitoring</li>
    </ul>
    <ul class="services services--extra">
      <li><svg class="tick" viewBox="0 0 11 9"><rect width="11" height="9" fill="var(--teal)"/><path d="M2 4.5 4.5 7 9 2" stroke="#fff" stroke-width="1.5" fill="none"/></svg>Succession Planning</li>
      <li><svg class="tick" viewBox="0 0 11 9"><rect width="11" height="9" fill="var(--teal)"/><path d="M2 4.5 4.5 7 9 2" stroke="#fff" stroke-width="1.5" fill="none"/></svg>Estate Planning</li>
      <li><svg class="tick" viewBox="0 0 11 9"><rect width="11" height="9" fill="var(--teal)"/><path d="M2 4.5 4.5 7 9 2" stroke="#fff" stroke-width="1.5" fill="none"/></svg>Cloud Solutions</li>
      <li><svg class="tick" viewBox="0 0 11 9"><rect width="11" height="9" fill="var(--teal)"/><path d="M2 4.5 4.5 7 9 2" stroke="#fff" stroke-width="1.5" fill="none"/></svg>Virtual CFO</li>
      <li><svg class="tick" viewBox="0 0 11 9"><rect width="11" height="9" fill="var(--teal)"/><path d="M2 4.5 4.5 7 9 2" stroke="#fff" stroke-width="1.5" fill="none"/></svg>The Wine Industry</li>
    </ul>

    <h2 class="why">WHY <span>CHOOSE US</span> ?</h2>
    <ul class="reasons">
      <li><svg class="tick" viewBox="0 0 11 9"><rect width="11" height="9" fill="var(--teal)"/><path d="M2 4.5 4.5 7 9 2" stroke="#fff" stroke-width="1.5" fill="none"/></svg><span>We are excellent at tax minimisation</span></li>
      <li><svg class="tick" viewBox="0 0 11 9"><rect width="11" height="9" fill="var(--teal)"/><path d="M2 4.5 4.5 7 9 2" stroke="#fff" stroke-width="1.5" fill="none"/></svg><span>All our staff truly care about getting the best result for our clients.</span></li>
      <li><svg class="tick" viewBox="0 0 11 9"><rect width="11" height="9" fill="var(--teal)"/><path d="M2 4.5 4.5 7 9 2" stroke="#fff" stroke-width="1.5" fill="none"/></svg><span>We take the time to listen and understand your circumstances and give you practical solutions for your concerns or enquiries.</span></li>
    </ul>

    <div class="cta">
      <span class="icon-dot"><svg width="16" height="16" viewBox="0 0 16 16"><circle cx="8" cy="5" r="3.2" fill="#fff"/><path d="M2 15c0-4 3-6 6-6s6 2 6 6z" fill="#fff"/></svg></span>
      <p class="cta-text">Call 0400 118 274 for<br>an appointment today</p>
    </div>

    <footer class="footer">
      <span><i></i>12 Harbour Lane Seaford Vic 3198</span>
      <span><i></i>www.lanternwellgroup.com.au</span>
    </footer>
  </section>

</div>
</body>
</html>
```